Business Card Design Project

Use newly designed logo and tie into newly designed website
I need a new logo and website layout designed for my partner's business. This is a birthday present. His business is interior painting, wallpapering and design. He also has access to a wide variety of products including carpet, fabrics, furniture, wallpaper, tile, countertops, etc. I have attached some screen shots of his website for reference. He is a one man shop and has a stellar reputation with his customers. He is on-time, very tidy, excellent with animals, and always finishes on time and on budget. There are no restrictions on colors or fonts. The logo needs to work well with the website, business cards and printed materials. The website needs to flow content for device size so it looks just as good on a cell phone or tablet as it does on a desktop computer. Whatever the heck that's called!Thanks. I am looking forward to seeing everyone's ideas.
Updates
Hi Designers,
We've reopened this project as our logo design project has just completed.
Please refer to the uploaded files and make use of either Horizontal or Vertical versions of the logo depending on what you think is suitable for your design proposals.
We look forward to your creative submissions!
Target Market(s)
Consumers looking to improve the interior environment of their homes by updating wall paint or paper, flooring (either carpet, tile, or hardwoods), counter tops, window treatments, etc. Clients tend to be more upper middle class and have certain taste levels and expectations. New logo, website and business card should align to meet those levels.
Industry/Entity Type
Cell Phone
Look and feel
Each slider illustrates characteristics of the customer's brand and the style your logo design should communicate.

```html
<!DOCTYPE html>
<html lang="en">
<head>
<meta charset="utf-8">
<title>Verity Interior Designs – Business Card</title>
<link rel="stylesheet" href="https://fonts.googleapis.com/css2?family=Cinzel:wght@400;500&display=swap">
<style>
  :root {
    --tan: #a88f62;
    --navy: #160a35;
    --wine: #8b1c1e;
    --orange: #fd9a0a;
    --paper: #ffffff;
    --backdrop: #e9e7e3;
    --ink-soft: #9c8459;
  }
  * { box-sizing: border-box; margin: 0; padding: 0; }
  html, body { width: 1200px; height: 1000px; overflow: hidden; }
  body {
    background: var(--backdrop);
    display: flex;
    align-items: center;
    justify-content: center;
    gap: 40px;
  }
  .card {
    width: 520px;
    height: 300px;
    position: relative;
    box-shadow: 0 6px 20px rgba(0,0,0,.18);
    overflow: hidden;
  }
  /* Back face */
  .card-back {
    display: grid;
    grid-template-columns: 1fr 1fr;
    grid-template-rows: 1fr 1fr;
  }
  .block-tan { background: var(--tan); }
  .block-navy { background: var(--navy); }
  .block-wine { background: var(--wine); }
  .block-orange { background: var(--orange); }
  .back-mark {
    position: absolute;
    left: 50%; top: 50%;
    transform: translate(-50%, -50%);
    width: 170px; height: 130px;
    background: var(--paper);
    display: flex;
    align-items: center;
    justify-content: center;
    flex-direction: column;
    font-family: "Cinzel", serif;
    font-weight: 500;
    color: var(--navy);
    text-align: center;
    line-height: 1.2;
  }
  .back-mark .mark-name { font-size: 26px; letter-spacing: 2px; }
  .back-mark .mark-sub { font-size: 11px; letter-spacing: 2px; }
  /* Front face */
  .card-front { background: var(--paper); }
  .contact {
    position: absolute;
    left: 34px; bottom: 40px;
    font-family: "Cinzel", serif;
  }
  .contact .person {
    font-size: 22px;
    color: var(--navy);
    letter-spacing: 1px;
    margin-bottom: 6px;
  }
  .contact ul { list-style: none; }
  .contact li {
    display: flex;
    align-items: center;
    gap: 8px;
    font-size: 10px;
    color: var(--ink-soft);
    letter-spacing: .5px;
    line-height: 1.6;
    white-space: nowrap;
  }
  .contact li.phone { font-size: 19px; color: var(--orange); line-height: 1.3; }
  .contact svg { width: 9px; height: 9px; fill: var(--wine); flex: none; }
  .brand {
    position: absolute;
    right: 30px; top: 120px;
    display: flex;
    align-items: flex-end;
    gap: 10px;
    font-family: "Cinzel", serif;
    font-weight: 500;
    color: var(--navy);
  }
  .brand .brand-square { width: 44px; height: 44px; background: var(--orange); }
  .brand .brand-text { line-height: 1; }
  .brand .brand-name { font-size: 34px; letter-spacing: 1px; display: block; }
  .brand .brand-sub { font-size: 13px; letter-spacing: 1.5px; display: block; margin-top: 3px; }
</style>
</head>
<body>
  <section class="card card-back" aria-label="Card back">
    <div class="block-tan"></div>
    <div class="block-navy"></div>
    <div class="block-wine"></div>
    <div class="block-orange"></div>
    <div class="back-mark">
      <span class="mark-name">VERITY</span>
      <span class="mark-sub">INTERIOR DESIGNS</span>
    </div>
  </section>

  <section class="card card-front" aria-label="Card front">
    <div class="brand">
      <span class="brand-square"></span>
      <span class="brand-text">
        <span class="brand-name">VERITY</span>
        <span class="brand-sub">INTERIOR DESIGNS</span>
      </span>
    </div>
    <div class="contact">
      <p class="person">DANE VERITY</p>
      <ul>
        <li class="phone"><svg viewBox="0 0 10 10"><path d="M2 0h2l1 3-1.5 1a6 6 0 0 0 2.5 2.5L7 5l3 1v2a2 2 0 0 1-2 2A8 8 0 0 1 0 2a2 2 0 0 1 2-2z"/></svg>555-420-0184</li>
        <li><svg viewBox="0 0 10 10"><path d="M0 2h10v6H0z"/></svg>DANE@VERITYDESIGNS.COM</li>
        <li><svg viewBox="0 0 10 10"><circle cx="5" cy="5" r="5"/></svg>WWW.VERITYDESIGNS.COM</li>
        <li><svg viewBox="0 0 10 10"><path d="M5 0l5 5H8.5v5h-7V5H0z"/></svg>2480 W LINDEN CT • MARROWFIELD, OR 97000</li>
      </ul>
    </div>
  </section>
</body>
</html>
```